Startup but Passionate F&B Company with big dreams for the future and multiple brands needs business

We need a simple logo and typography design for business card usage for a new company in a bustling and modern city called Brindle Terrace Pte Ltd. We are an F&B company that owns multiple brands of small boutique and indie cafes and eateries. We offer artisanal and home made food created with passion using quality and fresh ingredient. We would like to remain relevant and grow in the future constantly adapting changes and testing new boundaries with our menu and offerings in line with moving tastes and times. Final design and colors should be simple, fresh but modern and will remain relevant in time to come. For fonts we prefer modern fonts such as avenir (meaning future/futuristic) or any other new and trendy font types.
Updates

Please include a logo design as well as typography on th name card.

Thanks

Industry/Entity Type

Boutique

Font styles to use
Other font styles liked:
• Avenir or any other modern looking fonts

Colors

Designer to choose colors to be used in the design.

Requirements
Must have
• Logo + typography

```html
<!DOCTYPE html>
<html lang="en">
<head>
<meta charset="utf-8">
<title>Brindle Terrace Pte Ltd — Business Card</title>
<link href="https://fonts.googleapis.com/css2?family=Jost:wght@400;600&display=swap" rel="stylesheet">
<style>
  :root {
    --backdrop: #e9e6e1;
    --card-paper: #efeeeb;
    --brand-red: #c4161c;
    --ink: #2b2b2b;
    --ink-soft: #4a4a4a;
  }
  html, body {
    margin: 0;
    width: 1200px;
    height: 918px;
    overflow: hidden;
    background: var(--backdrop);
  }
  .canvas {
    position: relative;
    width: 1200px;
    height: 918px;
  }
  .business-card {
    position: absolute;
    left: 150px;
    top: 200px;
    width: 900px;
    height: 518px;
    background: var(--card-paper);
    box-shadow: 0 10px 30px rgba(0,0,0,0.12);
    font-family: "Jost", sans-serif;
    color: var(--ink);
  }
  .brand-lockup {
    position: absolute;
    right: 60px;
    top: 56px;
    display: flex;
    align-items: flex-start;
    gap: 16px;
  }
  .brand-mark {
    width: 22px;
    height: 22px;
    background: var(--brand-red);
    margin-top: 18px;
  }
  .brand-name {
    margin: 0;
    font-weight: 400;
    font-size: 58px;
    line-height: 1.05;
    color: var(--ink);
    text-align: right;
  }
  .brand-name .legal-suffix {
    display: block;
    font-size: 22px;
    line-height: 1.4;
  }
  .person {
    position: absolute;
    left: 60px;
    top: 232px;
  }
  .person-name {
    margin: 0;
    font-weight: 600;
    font-size: 30px;
    letter-spacing: 1px;
    color: var(--brand-red);
  }
  .person-role {
    margin: 2px 0 0;
    font-size: 21px;
    color: var(--ink-soft);
  }
  .contact-list {
    position: absolute;
    left: 60px;
    top: 370px;
    margin: 0;
    padding: 0;
    list-style: none;
    font-size: 20px;
    color: var(--ink-soft);
  }
  .contact-list li {
    display: flex;
    align-items: center;
    gap: 12px;
    margin-bottom: 10px;
  }
  .contact-icon {
    width: 16px;
    height: 16px;
    flex: none;
  }
  .address {
    position: absolute;
    right: 60px;
    bottom: 50px;
    margin: 0;
    font-style: normal;
    font-size: 20px;
    line-height: 1.35;
    color: var(--ink-soft);
  }
</style>
</head>
<body>
<div class="canvas">
  <article class="business-card">
    <div class="brand-lockup">
      <h1 class="brand-name">Brindle<br>Terrace<span class="legal-suffix">Pte Ltd</span></h1>
      <span class="brand-mark" aria-hidden="true"></span>
    </div>

    <div class="person">
      <p class="person-name">ALEX TAN</p>
      <p class="person-role">Director</p>
    </div>

    <ul class="contact-list">
      <li>
        <svg class="contact-icon" viewBox="0 0 16 16" aria-hidden="true">
          <rect width="16" height="16" rx="3" fill="var(--brand-red)"/>
          <path d="M5 3.5l1.6 2.4-1 1c.6 1.3 1.5 2.2 2.6 2.8l1-1 2.3 1.5-.8 1.8c-3.4-.3-6.3-3.2-6.6-6.7z" fill="#fff"/>
        </svg>
        <span>0198 765 432</span>
      </li>
      <li>
        <svg class="contact-icon" viewBox="0 0 16 16" aria-hidden="true">
          <rect width="16" height="16" rx="3" fill="var(--brand-red)"/>
          <rect x="3" y="4.5" width="10" height="7" fill="none" stroke="#fff" stroke-width="1.2"/>
          <path d="M3 4.8l5 3.8 5-3.8" fill="none" stroke="#fff" stroke-width="1.2"/>
        </svg>
        <span>alextan@BrindleTerrace.com</span>
      </li>
    </ul>

    <address class="address">42 Harbour Lane<br>Riverside, Any City</address>
  </article>
</div>
</body>
</html>
```